Website for a health information tech company

I need a website for a new startup company, Lumivale, Inc. that specializes in healthcare information technology. Lumivale is a monitoring system that uses wearable sensors and predictive algorithms to detect when an elderly persons health is declining and triggers progressively higher levels of interventions.

The site needs to be very simple, elegant and initially will have minimal information as company and product is still under development and is in a stealth mode. I like the tandovix.com website as it has a "single page" look and feel with sliding vertical sections. Ideally the sections would be "Home", "Technology", "Customers", "News", "About Us" and "Contact Us". The contact us should have a contact form that gets sent to an email address.

I have a couple of example sites that my site should take inspiration from (tandovix.com and brimholtway.com). I would like a WordPress backend so I can easily update content so the winning design should be easily importable or setup into Wordpress.

Target Market(s)

Investors, Customers (Doctors, Patients, Health Insurance companies, Hospital directors)

Industry/Entity Type

Healthcare

Requirements
Must have
• top horizontal menu that gets repeated on each vertical slide. Should have animated vertical slides. Must be viewable on any device (iPad, Android Tablets) correctly and must render correctly on different screen sizes. Must be viewable in all popular browsers. Must work well with touchscreen devices such as iPad, iPhone, Android tablets and phones.
Must have a content management system backend such as WordPress so I can edit/update content and in future add additional sections, images etc.

See attached company logo so colors must be complimentary to the logo colors. Feel free to use the logo colors as web site theme colors if it makes sense.
Nice to have
• Nice subtle textured background like linen or leather.
Should not have
• Not looking for traditional web site design with nav bars on left etc
Should not feel like a traditional web site where you click a link and another page loads. It must be animated slide into a different section. No flash or any other technology that requires plug ins.

```html
<!DOCTYPE html>
<html lang="en">
<head>
<meta charset="utf-8">
<title>Lumivale — Complete Care For You</title>
<link href="https://fonts.googleapis.com/css2?family=Oswald:wght@400&family=Ubuntu:wght@400;500;700&display=swap" rel="stylesheet">
<style>
  :root{
    --orange:#f28a1a;
    --orange-light:#ffb347;
    --orange-dark:#d96f00;
    --ink:#2b2b2b;
    --text:#3a3a3a;
    --muted:#555;
    --nav-top:#2a2a2a;
    --nav-bottom:#050505;
    --nav-line:#3d3d3d;
    --page-top:#f1f1f1;
    --page-low:#ebe7ef;
    --gold-a:#c08a2e;
    --gold-b:#e6c068;
    --white:#ffffff;
    --dot:#dcdcdc;
    --dot-active:#e2401f;
    --player:#000;
    --bar:#e0e0e0;
    --progress:#e8231d;
  }
  *{box-sizing:border-box;margin:0;padding:0}
  html,body{width:1200px;height:1130px;overflow:hidden}
  body{
    position:relative;
    font-family:"Ubuntu",sans-serif;
    color:var(--text);
    background:linear-gradient(to bottom,var(--page-top) 0,var(--page-top) 330px,var(--page-low) 660px,var(--page-low) 100%);
  }
  .gold-band{
    position:absolute;left:0;top:330px;width:1200px;height:330px;
    border-top:4px solid var(--white);
    background:linear-gradient(100deg,var(--gold-a) 0%,var(--gold-b) 30%,var(--gold-b) 70%,var(--gold-a) 100%);
  }

  /* header */
  .brand{position:absolute;left:80px;top:178px;display:flex;align-items:center;gap:14px}
  .brand-mark{width:34px;height:34px;border-radius:50%;background:var(--orange)}
  .brand-name{font-family:"Ubuntu",sans-serif;font-weight:500;font-size:50px;color:var(--orange);letter-spacing:-0.5px}

  .topbar{position:absolute;top:20px;left:648px;height:32px;display:flex;align-items:center;font-weight:700;font-size:16px;color:var(--ink)}
  .topbar .phone{display:flex;align-items:center;gap:12px}
  .topbar .touch{margin-left:58px;letter-spacing:.2px}
  .socials{display:flex;gap:8px;margin-left:22px}
  .socials span{width:36px;height:36px;border-radius:50%;background:linear-gradient(#5a9ad8,#2c64b0)}
  .socials span.video{background:linear-gradient(#e0e0e0,#b5b5b5)}

  .main-nav{
    position:absolute;left:421px;top:193px;width:728px;height:52px;
    background:linear-gradient(var(--nav-top),var(--nav-bottom));
    border:1px solid #000;box-shadow:0 0 0 1px #777 inset;
    display:flex;
  }
  .main-nav a{
    display:flex;align-items:center;justify-content:center;
    color:var(--orange);text-decoration:none;font-size:17px;
    border-right:1px solid var(--nav-line);height:100%;
  }
  .main-nav a:last-child{border-right:none}

  /* slider */
  .slider{
    position:absolute;left:52px;top:286px;width:1097px;height:417px;
    background:var(--white);box-shadow:0 3px 8px rgba(0,0,0,.35);
  }
  .slide-photo{
    position:absolute;left:55px;top:6px;width:546px;height:392px;
    background:linear-gradient(to bottom,#f4f4f4 0%,#e6ebee 55%,#ffffff 100%);
  }
  .slide-copy{position:absolute;left:641px;top:36px;width:430px}
  .slide-copy h2{font-family:"Oswald",sans-serif;font-weight:400;font-size:35px;color:var(--orange);line-height:1.2;letter-spacing:.3px}
  .slide-copy p{margin-top:14px;font-size:16.5px;line-height:26.3px;color:var(--ink)}
  .btn-more{
    position:absolute;left:641px;top:281px;width:192px;height:48px;
    background:linear-gradient(var(--orange-light),var(--orange));
    border:1px solid var(--orange-dark);
    display:flex;align-items:center;padding-left:19px;gap:12px;
    font-family:"Oswald",sans-serif;font-size:21px;color:#5a3300;text-decoration:none;
  }
  .dots{position:absolute;left:291px;top:394px;display:flex;gap:9px}
  .dots span{width:11px;height:11px;border-radius:50%;background:var(--dot);box-shadow:inset 0 1px 2px rgba(0,0,0,.25)}
  .dots span.active{background:var(--dot-active)}

  /* welcome */
  .welcome{position:absolute;left:60px;top:740px;width:540px}
  .welcome h1{font-family:"Oswald",sans-serif;font-weight:400;font-size:35px;color:var(--orange);line-height:1.2}
  .welcome h3{margin-top:6px;font-size:14px;font-weight:700;color:var(--ink);letter-spacing:.2px}
  .welcome p{margin-top:12px;font-size:14.3px;line-height:21px;color:var(--muted)}
  .welcome p + p{margin-top:21px}

  /* video */
  .video{position:absolute;left:623px;top:748px;width:526px;height:362px;background:var(--player)}
  .video .replay{position:absolute;left:215px;top:137px;display:flex;align-items:center;gap:8px;color:var(--white);font-size:18px}
  .video .replay i{width:30px;height:24px;border-radius:4px;background:linear-gradient(#fafafa,#9c9c9c)}
  .video .headline{position:absolute;left:0;width:100%;top:188px;text-align:center;color:var(--white);font-weight:700;font-size:24px}
  .controls{position:absolute;left:0;bottom:0;width:100%;height:28px;background:linear-gradient(#f4f4f4,#cfcfcf);display:flex;align-items:center;font-size:12px;color:#333}
  .controls .time{margin-left:8px}
  .controls .track{margin-left:14px;width:300px;height:6px;background:var(--progress);border-radius:3px;position:relative}
  .controls .track::after{content:"";position:absolute;right:-6px;top:-4px;width:14px;height:14px;border-radius:50%;background:#eee;border:1px solid #666}
</style>
</head>
<body>
  <div class="gold-band"></div>

  <header>
    <div class="brand">
      <span class="brand-mark"></span>
      <span class="brand-name">Lumivale</span>
    </div>

    <div class="topbar">
      <div class="phone">
        <svg width="26" height="30" viewBox="0 0 26 30" aria-hidden="true">
          <path d="M6 2c2 0 3 5 3 6s-3 2-3 3c0 3 4 9 7 10 1 0 2-3 3-3s6 2 6 4-3 4-5 4C9 26 2 14 2 7c0-3 2-5 4-5z" fill="#c8281e"/>
          <path d="M4 28h20" stroke="#888" stroke-width="1.5"/>
        </svg>
        <span>555-0142-7731</span>
      </div>
      <span class="touch">KEEP IN TOUCH</span>
      <div class="socials">
        <span></span><span></span><span class="video"></span>
      </div>
    </div>

    <nav class="main-nav">
      <a href="#home" style="width:99px">HOME</a>
      <a href="#technology" style="width:141px">TECHNOLOGY</a>
      <a href="#customers" style="width:133px">CUSTOMERS</a>
      <a href="#news" style="width:84px">NEWS</a>
      <a href="#about" style="width:118px">ABOUT US</a>
      <a href="#contact" style="flex:1">CONTACT US</a>
    </nav>
  </header>

  <section class="slider">
    <div class="slide-photo" role="img" aria-label="Two doctors attending an elderly patient resting in a hospital bed"></div>
    <div class="slide-copy">
      <h2>COMPLETE CARE FOR YOU.......</h2>
      <p>Lorem ipsum dolor sit amet, consectetur adipiscing elit. Proin placerat ac arcu vitae hendrerit. Donec accumsan dignissim ligula, ut aliquam est condimentum eu. Aenean laoreet nisi eu sodales hendrerit. Maecenas nulla risus, auctor id diam vel, dictum gravida elit. Curabitur non sagittis turpis. Maecenas nulla risus, auctor id diam lit.</p>
    </div>
    <a class="btn-more" href="#technology">KNOW MORE
      <svg width="26" height="26" viewBox="0 0 26 26" aria-hidden="true">
        <circle cx="13" cy="13" r="11" fill="none" stroke="#fff" stroke-width="2"/>
        <path d="M8 13h9M13 8.5l4.5 4.5-4.5 4.5" fill="none" stroke="#fff" stroke-width="2.2"/>
      </svg>
    </a>
    <div class="dots"><span class="active"></span><span></span><span></span><span></span><span></span><span></span></div>
  </section>

  <section class="welcome">
    <h1>WELCOME TO LUMIVALE</h1>
    <h3>NAM PURUS URNA, PLACERAT ADIPISCING EUISMOD SIT AMET.</h3>
    <p>Nunc interdum erat quis feugiat hendrerit. Suspendisse nec felis nec arcu aliquet malesuada. Vestibulum malesuada libero non lorem placerat, ut tempor ligula lacinia. Nulla in tincidunt purus. Vestibulum nisl nunc, vestibulum quis tempor molestie, blandit eu eros. Integer non elementum elit, eu lacinia tortor. Nunc justo nulla, suscipit quis urna sit amet, aliquet consectetur felis. Mauris ullamcorper neque id libero consequat, vitae pretium dui tempor. Suspendisse potenti.</p>
    <p>Vestibulum eu tortor eu nulla gravida posuere et quis elit. Vestibulum euismod neque leo, vitae mattis risus sollicitudin venenatis. Suspendisse at iaculis eros. Fusce sit amet urna auctor, cursus dolor nec, molestie nisl. Praesent mattis velit diam, nec adipiscing neque interdum ut.</p>
  </section>

  <section class="video">
    <div class="replay"><i></i>Replay</div>
    <div class="headline">SEE US IN&nbsp; ACTION!</div>
    <div class="controls">
      <svg width="30" height="28" viewBox="0 0 30 28" aria-hidden="true"><path d="M11 8l9 6-9 6z" fill="#222"/><path d="M29 3v22" stroke="#aaa"/></svg>
      <svg width="30" height="28" viewBox="0 0 30 28" aria-hidden="true"><path d="M6 11h4l5-4v14l-5-4H6z" fill="#222"/><path d="M18 10v8M21 8v12" stroke="#444" stroke-width="1.5"/><path d="M29 3v22" stroke="#aaa"/></svg>
      <span class="time">3:12 / 3:12</span>
      <div class="track"></div>
      <svg style="margin-left:auto" width="70" height="28" viewBox="0 0 70 28" aria-hidden="true">
        <path d="M1 3v22" stroke="#aaa"/>
        <path d="M12 8h5M12 8v5M30 8h-5M30 8v5M12 20h5M12 20v-5M30 20h-5M30 20v-5" stroke="#222" stroke-width="2"/>
        <path d="M40 3v22" stroke="#aaa"/>
        <rect x="46" y="8" width="20" height="12" rx="3" fill="#333"/>
        <path d="M50 16l6-5 6 5z" fill="#fff"/>
      </svg>
    </div>
  </section>
</body>
</html>
```